Furniture retail store requires in store display board design.

I am launching a new bed buying concept in my retail stores and require a point of sale graphic to explain the purchase process to consumers.
1.Select base style.(Including headboard) + 2. Customise legs and storage options. + 3.Choose Colours. + 4. Add your perfect mattress. = Your perfect nights sleep.
I'm imagining a sketchy/whiteboard/chalkboard type effect. The main boards will hang above a bed and will be 150cm wide x 35cm high.
Consumers 30yo+
Retail

```html
<!DOCTYPE html>
<html lang="en">
<head>
<meta charset="utf-8">
<title>Build Your Bed – Display Board</title>
<link rel="stylesheet" href="https://fonts.googleapis.com/css2?family=Bebas+Neue&family=Rochester&family=Lobster&display=block">
<style>
  :root {
    --chalkboard: #1c1b1b;
    --chalkboard-light: #302e2d;
    --chalk-dust: rgba(255, 255, 255, 0.05);
    --step-yellow: #f4cf1b;
    --step-orange: #f28a1c;
    --step-green: #a6d22b;
    --step-blue: #22a2e2;
    --result-red: #e3201e;
    --room-yellow: #f2b705;
    --room-amber: #e79a04;
    --room-floor: #8e8b86;
  }
  * { margin: 0; padding: 0; box-sizing: border-box; }
  html, body { width: 1200px; height: 280px; overflow: hidden; background: #fff; }
  .board {
    position: relative;
    width: 1200px;
    height: 280px;
    overflow: hidden;
    background:
      radial-gradient(ellipse 260px 70px at 180px 60px, var(--chalk-dust), transparent 70%),
      radial-gradient(ellipse 300px 60px at 620px 230px, var(--chalk-dust), transparent 70%),
      radial-gradient(ellipse 200px 90px at 760px 40px, rgba(255,255,255,0.04), transparent 70%),
      radial-gradient(ellipse 220px 60px at 330px 250px, rgba(255,255,255,0.035), transparent 70%),
      repeating-linear-gradient(-8deg, rgba(255,255,255,0.012) 0 2px, transparent 2px 7px),
      radial-gradient(ellipse at 35% 45%, var(--chalkboard-light) 0%, var(--chalkboard) 75%);
  }
  .bedroom-scene {
    position: absolute;
    inset: 0;
    width: 1200px;
    height: 280px;
  }
  .steps {
    position: absolute;
    left: 22px;
    top: 26px;
    list-style: none;
    font-family: "Bebas Neue", "Oswald", sans-serif;
    font-size: 36px;
    line-height: 57px;
    white-space: nowrap;
    transform: scaleX(0.88);
    transform-origin: left top;
    text-shadow: 0 0 1px rgba(0,0,0,0.4);
  }
  .step--base { color: var(--step-yellow); }
  .step--legs { color: var(--step-orange); }
  .step--colours { color: var(--step-green); }
  .step--mattress { color: var(--step-blue); }
  .equals {
    position: absolute;
    left: 486px;
    top: 156px;
    width: 60px;
    height: 30px;
  }
  .equals span {
    position: absolute;
    left: 0;
    width: 60px;
    height: 10px;
    background: var(--result-red);
    border-radius: 2px;
    transform: rotate(-4deg);
  }
  .equals span:first-child { top: 0; }
  .equals span:last-child { bottom: 0; }
  .result {
    position: absolute;
    left: 572px;
    top: 92px;
    font-family: "Rochester", "Lobster", cursive;
    color: var(--result-red);
    font-size: 54px;
    line-height: 66px;
    white-space: nowrap;
    transform: rotate(-10deg);
    transform-origin: left top;
  }
  .result .line { display: block; }
  .result .line--second { padding-left: 40px; }
</style>
</head>
<body>
  <main class="board">
    <svg class="bedroom-scene" viewBox="0 0 1200 280" role="img" aria-label="Photo of a made double bed with white bedding and bedside lamps against a bright yellow wall">
      <defs>
        <linearGradient id="wall" x1="0" y1="0" x2="1" y2="1">
          <stop offset="0" stop-color="var(--room-yellow)"/>
          <stop offset="1" stop-color="var(--room-amber)"/>
        </linearGradient>
        <linearGradient id="floor" x1="0" y1="0" x2="0" y2="1">
          <stop offset="0" stop-color="#b5b1aa"/>
          <stop offset="1" stop-color="var(--room-floor)"/>
        </linearGradient>
      </defs>
      <polygon points="908,0 1200,0 1200,280 882,280" fill="url(#wall)"/>
      <polygon points="886,250 1200,250 1200,280 882,280" fill="url(#floor)"/>
    </svg>

    <ol class="steps">
      <li class="step step--base">1. Select base style (includingheadboard) +</li>
      <li class="step step--legs">2. Customise legs and storage options +</li>
      <li class="step step--colours">3. Choose colours +</li>
      <li class="step step--mattress">4.&nbsp; Add your perfect mattress</li>
    </ol>

    <div class="equals" aria-label="equals"><span></span><span></span></div>

    <p class="result">
      <span class="line">Your Perfect</span>
      <span class="line line--second">Nights Sleep</span>
    </p>
  </main>
</body>
</html>
```